Web Design - 1 page for Buy - Repair - Service - Upgrade - PC Maintenance

We specialize in consumer and small business. It will be mobile friendly, viewable on all devices. Fully editable at the text level of the sections !!! - HTML / CSS only to be able to add a section would be to the web site
Updates

Add 200 Euro to project

Target Market(s)

consumer and small business IT.

Coding

Coded - Design and coding required

Number of Pages Required

1 page

Font styles to use
Sans Serif

Requirements
Must have
• Looking for a page with a design that compliments the business card and pamphlet that has already been made (attached files). It should look professional and easy to read business. Email and phone number should be visible when the page loads. I do not want any forms for people to mess with. No "Contact Us" form or enter in email for newsletter. Customers will just be looking for this site to confirm we are professionals and have our business in order. OpenStreetMap: embedding map in webpage (like Google Maps) to where the workshop is located
Nice to have
• 4tulva.com => this style of website would be more modern visually by integrating higher demands

```html
<!DOCTYPE html>
<html lang="en">
<head>
<meta charset="utf-8">
<title>Norvale Tech – Buy, Repair, Service, Upgrade</title>
<link rel="stylesheet" href="https://fonts.googleapis.com/css2?family=Montserrat:wght@500;600&family=Nunito+Sans:wght@400;700;800&display=swap">
<style>
  :root {
    --brand-blue: #4a86c5;
    --brand-blue-light: #6fb6ef;
    --ink: #333333;
    --nav-grey: #666666;
    --logo-grey: #5e5e5e;
    --white: #ffffff;
    --art-violet: #8f7ae6;
    --art-sky: #bfe8fb;
  }
  * { box-sizing: border-box; margin: 0; padding: 0; }
  html, body { width: 1200px; height: 729px; overflow: hidden; background: var(--white); }
  .page {
    position: relative;
    width: 1200px;
    height: 729px;
    overflow: hidden;
    font-family: "Nunito Sans", sans-serif;
    color: var(--ink);
  }

  /* Contact bar */
  .contact-bar {
    position: absolute;
    top: 0; right: 0;
    width: 576px; height: 43px;
  }
  .contact-bar__shape { position: absolute; inset: 0; }
  .contact-bar__item {
    position: absolute;
    top: 0; height: 43px;
    display: flex; align-items: center; gap: 8px;
    color: var(--white);
    font-family: "Montserrat", sans-serif;
    font-weight: 600;
    font-size: 15.5px;
  }
  .contact-bar__item--phone { left: 42px; }
  .contact-bar__item--email { left: 218px; }
  .contact-bar__social { position: absolute; top: 10px; left: 470px; display: flex; gap: 4px; }
  .social-dot { width: 23px; height: 23px; border: 1.6px solid var(--white); border-radius: 50%; }

  /* Brand */
  .brand {
    position: absolute;
    top: 88px; left: 30px;
    display: flex; align-items: center; gap: 10px;
    font-family: "Nunito Sans", sans-serif;
    font-weight: 800;
    font-size: 30px;
    color: var(--brand-blue);
    letter-spacing: 0.5px;
  }
  .brand__mark { width: 18px; height: 18px; background: var(--logo-grey); }

  /* Navigation */
  .main-nav {
    position: absolute;
    top: 80px; left: 671px;
    display: flex; gap: 41px;
    font-family: "Montserrat", sans-serif;
    font-weight: 500;
    font-size: 15px;
    color: var(--nav-grey);
    list-style: none;
  }
  .main-nav__link--active { color: var(--brand-blue); }

  /* Hero */
  .hero-art {
    position: absolute;
    left: 52px; top: 151px;
    width: 488px; height: 460px;
    border-radius: 24px;
    background: linear-gradient(150deg, var(--art-sky) 0%, var(--brand-blue-light) 45%, var(--art-violet) 100%);
    opacity: 0.55;
  }
  .hero-copy { position: absolute; left: 593px; top: 262px; width: 560px; }
  .hero-copy__title { font-weight: 800; font-size: 38px; line-height: 1.15; letter-spacing: -0.2px; }
  .hero-copy__text { margin-top: 2px; font-size: 21px; line-height: 28.5px; }
  .hero-copy__button {
    display: flex; align-items: center; justify-content: center;
    margin-top: 33px; margin-left: -3px;
    width: 246px; height: 48px;
    border: 2px solid var(--brand-blue);
    border-radius: 24px;
    color: var(--brand-blue);
    font-weight: 700; font-size: 20px;
    text-decoration: none;
  }
</style>
</head>
<body>
<div class="page">
  <div class="contact-bar">
    <svg class="contact-bar__shape" width="576" height="43" viewBox="0 0 576 43">
      <polygon points="0,0 576,0 576,43 22,43" fill="var(--brand-blue)"/>
    </svg>
    <span class="contact-bar__item contact-bar__item--phone">
      <svg width="22" height="22" viewBox="0 0 22 22" aria-hidden="true">
        <circle cx="11" cy="11" r="9.8" fill="none" stroke="#fff" stroke-width="1.6"/>
        <path d="M7.5 6.5c.5-.5 1.2-.5 1.5 0l1 1.6c.3.5.1 1-.3 1.3l-.6.4c.5 1.2 1.5 2.3 2.8 2.9l.5-.6c.3-.4.9-.5 1.3-.2l1.5 1c.5.3.5 1 0 1.5l-.7.7c-.7.7-2 .6-3.5-.3-1.8-1.1-3.2-2.6-4.1-4.4-.7-1.4-.7-2.6 0-3.3z" fill="#fff"/>
      </svg>
      1800.555.0142
    </span>
    <span class="contact-bar__item contact-bar__item--email">
      <svg width="22" height="22" viewBox="0 0 22 22" aria-hidden="true">
        <circle cx="11" cy="11" r="9.8" fill="none" stroke="#fff" stroke-width="1.6"/>
        <rect x="6" y="7.5" width="10" height="7" rx="1" fill="none" stroke="#fff" stroke-width="1.4"/>
        <path d="M6.3 8l4.7 3.6L15.7 8" fill="none" stroke="#fff" stroke-width="1.4"/>
      </svg>
      info@norvaletech.com
    </span>
    <div class="contact-bar__social">
      <span class="social-dot"></span><span class="social-dot"></span><span class="social-dot"></span>
    </div>
  </div>

  <div class="brand"><span class="brand__mark"></span>NORVALE TECH</div>

  <ul class="main-nav">
    <li class="main-nav__link main-nav__link--active">HOME</li>
    <li class="main-nav__link">ABOUT</li>
    <li class="main-nav__link">SERVICES</li>
    <li class="main-nav__link">WHY US?</li>
    <li class="main-nav__link">CONTACT</li>
  </ul>

  <div class="hero-art" role="img" aria-label="Isometric illustration of a team building a website on a large monitor, with a ladder, bar chart, gears and a magnifying glass"></div>

  <div class="hero-copy">
    <h1 class="hero-copy__title">Welcome to Norvale Tech</h1>
    <p class="hero-copy__text">Lorem ipsum dolor sit amet, consectetur adipiscing elit, sed do eiusmod tempor incididunt ut labore et dolore magna aliqua. Ut enim ad minim veniam, quis nostrud exercitation ullamco laboris nisi ut aliquip ex ea commodo consequat.</p>
    <a class="hero-copy__button" href="#services">Get Started</a>
  </div>
</div>
</body>
</html>
```